Commercial Real Estate Company Needs an Awesome Flyer Design for their Oceanfront Property

We need a 2-page flyer or our Class A Oceanfront Property in Santa Monica, California. Approximately 16,149 square feet of Class A rare oceanfront office space with private balconies will be in available 4th Quarter of 2014. The SPACE has not been on the market for over 20 YEARS!

I attached our Previous 2-page flyer for the 2,353 square feet. We need a new vibrant, modern flyer that will attract Tech, Entertainment, Financial, and Marketing Companies to our building. Also, the 2nd Floor Space Plan is attached.

Also, please check out our website www.verlindeproperty.com. We would like to use the colors of our website and logo to incorporate with the flyer.

I updated the Must Have's on the Listing!

Target Market(s)

Entertainment, Financial, Tech Companies

Industry/Entity Type

Real Estate

Requirements
Must have
• Our Company Logo, Company, Leasing Agents On the First and 2nd Page

Trevor L. Ashdown (310) 555-0142
trev@verlindeproperty.com

Mark Oda (310) 555-0187
mark@verlindeproperty.com

Verlinde Property.
5127 N Harlow Ave, Suite 210
West Hollywood, Ca. 90069
(310) 555-0142
www.verlindeproperty.com

Also, the Front Page should indicate

"Rare Class A Oceanfront Office Space in the heart of Santa Monica"
"2nd Floor Office Space consisting of 16,159 square feet with private balconies."
Nice to have
• Please use description of the office building. You can omit whatever you think is unnecessary

"Bellhaven Court is one of Santa Monica's rare commercial properties that is both strategically located in the city's burgeoning central business district, yet ideally positioned on palm-lined Ocean Ave directly across from the Pacific Ocean. Built in 1987, the 3-story mixed-use commercial and retail property features prestigious retail Tenants such as Kelp Tavu and Dune Kitchen."

"A year-round coastal Mediterranean climate, a highly diverse business sector, and the vibrant, pedestrian-oriented Linden Row Walkway and Harbor Crest Arcade makes this beachside community a highly desirable commercial and retail location."

```html
<!DOCTYPE html>
<html lang="en">
<head>
<meta charset="utf-8">
<title>Bellhaven Court – Verlinde Property</title>
<link rel="stylesheet" href="https://fonts.googleapis.com/css2?family=Roboto+Condensed:wght@300;400;700&display=swap">
<style>
  :root {
    --backdrop: #4a4646;
    --paper: #ffffff;
    --brand-yellow: #fdd31f;
    --brand-blue: #0f5cae;
    --brand-blue-deep: #0a4a94;
    --ink: #1c1c1c;
    --ink-soft: #333333;
  }
  * { margin: 0; padding: 0; box-sizing: border-box; }
  html, body { width: 882px; height: 1200px; overflow: hidden; }
  body {
    background: var(--backdrop);
    font-family: "Roboto Condensed", "Arial Narrow", sans-serif;
    position: relative;
  }
  .flyer {
    position: absolute; left: 60px; top: 107px;
    width: 762px; height: 985px;
    background: var(--paper);
    overflow: hidden;
  }
  .hero-photo {
    position: absolute; left: 0; top: 0; width: 762px; height: 403px;
    background: linear-gradient(180deg,
      #2f5fb4 0%, #3f70c2 18%, #8fa9cf 25%,
      #ece8e1 32%, #f1ede6 48%, #d8d2c8 62%,
      #c9c2b6 68%, #2c3565 74%, #3a3f58 82%,
      #8c8d94 88%, #b7b8bd 94%, #9a9ba1 100%);
  }
  .call-block { position: absolute; left: 39px; top: 30px; color: var(--paper); }
  .call-block .phone { font-weight: 300; font-size: 27px; letter-spacing: 0.3px; line-height: 1; }
  .call-block .web { font-weight: 700; font-size: 17px; margin-top: 7px; }

  .headline-band {
    position: absolute; left: 0; top: 403px; width: 762px; height: 120px;
    background: var(--brand-yellow);
  }
  .headline-band h1 {
    position: absolute; left: 67px; top: 16px;
    color: var(--paper); font-size: 38.5px; line-height: 47px;
    font-weight: 300; text-transform: uppercase; letter-spacing: 0.3px;
    white-space: nowrap;
  }
  .headline-band h1 strong { font-weight: 700; }
  .band-pointer { position: absolute; left: 69px; top: 523px; }

  .offer-panel {
    position: absolute; left: 0; top: 523px; width: 762px; height: 347px;
    background: linear-gradient(90deg, var(--brand-blue-deep) 0%, var(--brand-blue) 55%, #1566bd 100%);
  }
  .property-name {
    position: absolute; left: 64px; top: 40px;
    font-size: 62px; line-height: 1; color: var(--brand-yellow);
    text-transform: uppercase; font-weight: 300; white-space: nowrap;
  }
  .property-name strong { font-weight: 700; }
  .property-address {
    position: absolute; left: 62px; top: 112px;
    color: var(--paper); font-size: 29px; font-weight: 300; text-transform: uppercase;
  }
  .space-facts {
    position: absolute; left: 64px; top: 202px;
    color: var(--paper); font-size: 25px; line-height: 30px; font-weight: 700;
    text-transform: uppercase; white-space: nowrap;
  }
  .space-facts .accent { color: var(--brand-yellow); }
  .interior-frame {
    position: absolute; left: 426px; top: 121px; width: 294px; height: 195px;
    background: var(--paper); padding: 7px;
    box-shadow: 0 6px 10px rgba(0,0,0,0.35);
  }
  .interior-photo {
    width: 100%; height: 100%;
    background: linear-gradient(180deg, #f4f1ea 0%, #e6e0d2 35%, #cdbfa5 55%, #c08e4f 72%, #9a7a57 100%);
  }

  .contact-strip { position: absolute; left: 0; top: 870px; width: 762px; height: 115px; background: var(--paper); }
  .brand-mark { position: absolute; left: 32px; top: 20px; width: 100px; text-align: center; }
  .brand-mark .dot { width: 38px; height: 38px; border-radius: 50%; background: var(--brand-yellow); margin: 0 auto 9px; }
  .brand-mark .name { font-size: 11px; letter-spacing: 2.5px; color: var(--ink); font-weight: 400; line-height: 14px; text-transform: uppercase; }
  .contact-col { position: absolute; top: 27px; color: var(--ink-soft); font-size: 13.5px; line-height: 18px; }
  .contact-col h2 { font-size: 14.5px; font-weight: 700; color: var(--ink); text-transform: uppercase; margin-bottom: 7px; letter-spacing: 0.2px; }
  .contact-col.company { left: 159px; top: 30px; font-size: 12.5px; line-height: 17px; }
  .contact-col.company h2 { margin-bottom: 9px; }
  .contact-col.agent-one { left: 365px; }
  .contact-col.agent-two { left: 568px; }
  .divider { position: absolute; left: 350px; top: 20px; width: 1px; height: 74px; background: var(--ink-soft); }
</style>
</head>
<body>
  <main class="flyer">
    <div class="hero-photo" role="img" aria-label="Photo of the curved white three-story Bellhaven Court building on a palm-lined avenue under a blue sky, with navy storefront awnings at street level and a blue hotel tower behind"></div>
    <div class="call-block">
      <div class="phone">CALL : (310) 555-0142</div>
      <div class="web">www.verlindeproperty.com</div>
    </div>

    <section class="headline-band">
      <h1>Rare Class A <strong>Oceanfront Office<br>Space</strong> in the heart of <strong>Santa Monica</strong></h1>
    </section>

    <section class="offer-panel">
      <div class="property-name"><strong>Bellhaven</strong> Court</div>
      <div class="property-address">1718 Coral Avenue</div>
      <p class="space-facts">
        2nd Floor Office Space<br>
        Consisting of<br>
        <span class="accent">16,159</span> Square Feet<br>
        With <span class="accent">Private Balconies</span>
      </p>
      <div class="interior-frame">
        <div class="interior-photo" role="img" aria-label="Interior photo of the open second-floor office with a curved wooden reception desk and workstations"></div>
      </div>
    </section>

    <svg class="band-pointer" width="16" height="10" viewBox="0 0 16 10" aria-hidden="true">
      <polygon points="0,0 16,0 8,10" fill="#fdd31f"/>
    </svg>

    <footer class="contact-strip">
      <div class="brand-mark">
        <div class="dot"></div>
        <div class="name">Verlinde<br>Property</div>
      </div>
      <div class="contact-col company">
        <h2>Verlinde Property</h2>
        5127 N Harlow Ave, Suite 210<br>
        West Hollywood, Ca. 90069
      </div>
      <div class="divider"></div>
      <div class="contact-col agent-one">
        <h2>Trevor L. Ashdown</h2>
        (310) 555-0142<br>
        trev@verlindeproperty.com
      </div>
      <div class="contact-col agent-two">
        <h2>Mark Oda</h2>
        (310) 555-0187<br>
        mark@verlindeproperty.com
      </div>
    </footer>
  </main>
</body>
</html>
```